Residential home builder needs a fresh looking business card

We require a fresh looking business card for our business. We like the clean modern look. I have uploaded out logo and our email footer that incorporates some different elements. Blacks and Whites are good but i will leave this up to the design crowd creative minds.

our slogan is:
your idea of the perfect home

website (temporary site) but similar look and feel to the finished one
pinegrovedwellings.com.au

We also have intentions to apply the same look and feel to the rest of our stationary (letterheads, envelopes, site signs, vehicles etc)

Home Builder

```html
<!DOCTYPE html>
<html lang="en">
<head>
<meta charset="utf-8">
<title>Pinegrove Dwellings – Business Card</title>
<link rel="stylesheet" href="https://fonts.googleapis.com/css2?family=Open+Sans:wght@400;600;700&display=swap">
<style>
  :root {
    --canvas: #eeeeec;
    --paper: #ffffff;
    --ink: #2a2a2a;
    --gold: #e2be2b;
    --gold-deep: #d9b321;
    --shadow: rgba(0, 0, 0, 0.18);
  }
  * { margin: 0; padding: 0; box-sizing: border-box; }
  html, body { width: 1200px; height: 1200px; overflow: hidden; }
  body {
    background: var(--canvas);
    font-family: "Open Sans", Arial, sans-serif;
    color: var(--ink);
    position: relative;
  }
  .card {
    position: absolute;
    left: 150px;
    width: 900px;
    height: 514px;
    overflow: hidden;
    box-shadow: 0 14px 34px var(--shadow);
  }
  .card--front { top: 56px; background: var(--paper); }
  .card--back { top: 630px; background: var(--gold); }

  /* front */
  .brand {
    position: absolute;
    left: 70px;
    top: 214px;
    display: flex;
    align-items: center;
    gap: 14px;
  }
  .brand__mark {
    width: 26px;
    height: 26px;
    background: var(--gold);
  }
  .brand__name {
    font-weight: 600;
    font-size: 30px;
    color: var(--ink);
    letter-spacing: 0.5px;
  }
  .person {
    position: absolute;
    right: 70px;
    top: 72px;
    text-align: right;
  }
  .person__name { font-weight: 700; font-size: 38px; color: var(--ink); line-height: 1.2; }
  .person__role { font-weight: 700; font-size: 25px; color: var(--gold); margin-top: 4px; }
  .contact {
    position: absolute;
    right: 70px;
    top: 262px;
    text-align: right;
    font-size: 19px;
    line-height: 1.45;
    color: var(--ink);
  }
  .contact__label { color: var(--gold); font-weight: 600; }
  .contact__gap { display: inline-block; width: 10px; }
  .card__band { position: absolute; left: 0; bottom: 0; width: 900px; height: 70px; }

  /* back */
  .back__texture {
    position: absolute;
    inset: 0;
    background: linear-gradient(135deg, var(--gold) 0%, var(--gold-deep) 55%, var(--gold) 100%);
  }
  .back__brand {
    position: absolute;
    left: 0;
    right: 0;
    top: 50%;
    transform: translateY(-50%);
    display: flex;
    justify-content: center;
    align-items: center;
    gap: 18px;
  }
  .back__mark { width: 34px; height: 34px; background: var(--paper); }
  .back__name { font-weight: 600; font-size: 46px; color: var(--paper); letter-spacing: 1px; }
</style>
</head>
<body>

  <section class="card card--front" aria-label="Business card front">
    <div class="brand">
      <span class="brand__mark"></span>
      <span class="brand__name">Pinegrove Dwellings</span>
    </div>

    <div class="person">
      <p class="person__name">Marcus Ellery</p>
      <p class="person__role">General Manager</p>
    </div>

    <div class="contact">
      <p><span class="contact__label">Mobile:</span>0400 218 565</p>
      <p><span class="contact__label">Phone:</span>08 5550 0142<span class="contact__gap"></span><span class="contact__label">Fax:</span>08 5550 0187</p>
      <p><span class="contact__label">Email:</span>marcus@pinegrovedwellings.com.au</p>
      <p><span class="contact__label">Web:</span>www.pinegrovedwellings.com.au</p>
      <p>PO Box 4821, Harbour Vale DC, WA 6100</p>
    </div>

    <svg class="card__band" viewBox="0 0 900 70" aria-hidden="true">
      <polygon points="0,46 560,46 538,70 0,70" fill="var(--ink)"/>
      <polygon points="590,20 900,20 900,70 545,70" fill="var(--gold)"/>
    </svg>
  </section>

  <section class="card card--back" aria-label="Business card back">
    <div class="back__texture" role="img" aria-label="Faint house floor-plan line pattern in soft gold tones"></div>
    <div class="back__brand">
      <span class="back__mark"></span>
      <span class="back__name">Pinegrove Dwellings</span>
    </div>
  </section>

</body>
</html>
```